Velmora Partners - website for real estate investment company

Create a bold, modern website that reflects Velmora’s success, professionalism, and credibility.
The design must stand out while maintaining a polished, corporate tone. (bold, but understated)
The client just created a new logo, and the website design must be in sync with the logo design. Information about the logo colors, fonts, and message are in the attached design brief.
Updates

Target Market(s)

b2b: banks, brokers, institutional partners, vendors, and property sellers.

Industry/Entity Type

real estate investment company

Number of Pages Required

1 page

Font styles to use
Sans Serif

Colors

Designer to choose colors to be used in the design.

Requirements
Must have
• 1. homepage design (psd) 2. a top banner image (psd) for a default inner page
Nice to have
• please see attached design brief
Should not have

```html
<!DOCTYPE html>
<html lang="en">
<head>
<meta charset="utf-8">
<meta name="format-detection" content="telephone=no,email=no,address=no">
<title>Velmora Partners</title>
<link rel="stylesheet" href="https://fonts.googleapis.com/css2?family=Barlow:wght@400;500;600;700;800&family=Barlow+Condensed:wght@600;700&display=swap">
<style>
:root{
  --red:#d71f27;
  --ink:#4b4b4b;
  --text:#2a2a2a;
  --muted:#555;
  --panel:#f1f1f1;
  --line:#e2e2e2;
  --footer:#111;
  --footer-text:#dddddd;
  --white:#fff;
}
*{margin:0;padding:0;box-sizing:border-box}
html,body{width:691px;height:1200px;overflow:hidden;background:var(--white);font-family:"Barlow",sans-serif;color:var(--text)}
.page{position:relative;width:691px;height:1200px}
.abs{position:absolute}
.nowrap{white-space:nowrap}
.brand{font-family:"Barlow",sans-serif;font-weight:800;letter-spacing:.5px;color:var(--ink);white-space:nowrap}
.site-header .brand{left:81px;top:13px;font-size:24px}
.main-nav span{position:absolute;top:22px;font-size:7.2px;color:var(--text);letter-spacing:.1px;white-space:nowrap}
.btn{background:var(--ink);color:var(--white);font-weight:700;display:flex;align-items:center;justify-content:center;overflow:hidden;white-space:nowrap}
.btn::before{content:"";position:absolute;left:0;top:0;border-top:7px solid var(--red);border-right:7px solid transparent}
.header-cta{left:544px;top:14px;width:66px;height:24px;font-size:7.2px}
.hero{left:0;top:51px;width:691px;height:322px;background:linear-gradient(180deg,#5fb5e6 0%,#a9d5ee 38%,#7d96a8 62%,#4a6d8c 76%,#3b5f82 100%)}
.hero-title{left:0;top:122px;width:691px;text-align:center;font-family:"Barlow Condensed",sans-serif;font-weight:700;font-size:38px;letter-spacing:1.6px;color:#3d4a55;opacity:.85;white-space:nowrap}
.stat{width:166px;height:164px;top:336px;background:var(--white);box-shadow:0 6px 14px rgba(0,0,0,.08);text-align:center}
.stat::before{content:"";position:absolute;left:4px;top:4px;border-top:26px solid var(--red);border-right:26px solid transparent}
.stat svg{position:absolute;left:64px;top:18px;width:38px;height:38px}
.stat-num{position:absolute;left:0;top:62px;width:100%;font-family:"Barlow Condensed",sans-serif;font-size:32px;font-weight:600;color:var(--ink);white-space:nowrap}
.stat-label{position:absolute;left:0;top:100px;width:100%;font-size:10px;font-weight:700;letter-spacing:.3px}
.stat-sub{position:absolute;left:0;top:120px;width:100%;font-size:10px;white-space:nowrap}
.welcome-title{left:0;top:540px;width:691px;text-align:center;font-family:"Barlow Condensed",sans-serif;font-size:29px;color:var(--ink);white-space:nowrap}
.welcome-text{left:108px;top:577px;width:475px;text-align:center;font-size:11px;line-height:19px;color:var(--muted)}
.contact-panel{left:97px;top:690px;width:491px;height:302px;background:var(--panel)}
.panel-title{left:0;top:41px;width:491px;text-align:center;font-family:"Barlow Condensed",sans-serif;font-size:21px;color:var(--ink)}
.field{position:absolute;background:var(--white);border:1px solid var(--line);font-size:7.4px;color:#666;display:flex;align-items:flex-start;padding-top:11px;padding-left:30px}
.field svg{position:absolute;left:8px;top:9px;width:10px;height:10px}
.field::after{content:"";position:absolute;left:23px;top:9px;width:1px;height:11px;background:#ccc}
.submit{left:69px;top:234px;width:354px;height:31px;font-size:7.4px;letter-spacing:.3px}
.site-footer{left:0;top:992px;width:691px;height:208px;background:var(--footer);color:var(--white)}
.site-footer .brand{left:0;top:28px;width:691px;text-align:center;font-size:28px;color:var(--white)}
.footer-nav{left:0;top:81px;width:691px;display:flex;justify-content:center;gap:15px;font-size:7.4px;white-space:nowrap}
.info{top:117px;display:flex;gap:6px;align-items:center}
.info-icon{width:25px;height:24px;border:1px solid #444;display:flex;align-items:center;justify-content:center}
.info-icon svg{width:10px;height:10px}
.info b{display:block;font-size:7.4px;letter-spacing:.3px}
.info span{font-size:7.4px;color:var(--footer-text)}
.career{left:479px;top:117px;width:88px;height:24px;font-size:7.2px;background:#4f4f4f}
.divider{left:81px;top:1164px;width:529px;height:1px;background:#333}
.copyright{left:81px;top:1176px;font-size:7.4px;color:var(--footer-text)}
.social{top:1175px;width:14px;height:14px;border:1px solid #555}
</style>
</head>
<body>
<div class="page">
  <header class="site-header">
    <div class="abs brand">VELMORA</div>
    <nav class="main-nav">
      <span style="left:205px">HOME</span>
      <span style="left:240px">OUR STORY</span>
      <span style="left:292px">INVESTMENT STRATEGY</span>
      <span style="left:386px">WHAT SETS US APART</span>
      <span style="left:474px">OUR PORTFOLIO</span>
    </nav>
    <div class="abs btn header-cta">CONTACT US</div>
  </header>

  <section class="abs hero" role="img" aria-label="City skyline across the water under a blue sky"></section>
  <h1 class="abs hero-title">EXPERIENCE - STRATEGY - VISION</h1>

  <div class="abs stat" style="left:81px">
    <svg viewBox="0 0 40 40" fill="none" stroke="#d71f27" stroke-width="1.6" stroke-linejoin="round"><path d="M3 18l8-8 6 4 5-2 6 2 9 6"/><path d="M11 10l-8 8 10 14 4 2"/><path d="M37 18l-10 12-5 4-4-3 3-3M24 30l-4-4M27 26l-5-5"/><path d="M20 3v4M13 5l2 3M27 5l-2 3"/></svg>
    <div class="stat-num">1989</div><div class="stat-label">FOUNDED</div><div class="stat-sub">Over 35 Years Of Excellence</div>
  </div>
  <div class="abs stat" style="left:262px">
    <svg viewBox="0 0 40 40" fill="none" stroke="#d71f27" stroke-width="1.6"><circle cx="14" cy="12" r="5"/><circle cx="14" cy="12" r="8" stroke-dasharray="3 2"/><path d="M22 12h6M28 6v12M28 6h4M28 18h4"/><circle cx="34" cy="6" r="2"/><circle cx="34" cy="18" r="2"/><path d="M3 30h8l8-3h8l7-4 2 2-10 8H3"/></svg>
    <div class="stat-num">23,000+</div><div class="stat-label">UNITS MANAGED</div><div class="stat-sub">Multifamily &amp; Healthcare</div>
  </div>
  <div class="abs stat" style="left:444px">
    <svg viewBox="0 0 40 40" fill="none" stroke="#d71f27" stroke-width="1.6"><path d="M16 4h8l-2 6h-4z"/><path d="M18 10c-8 4-10 14-6 22h16c4-8 2-18-6-22"/><path d="M23 17h-4a2 2 0 000 4h2a2 2 0 010 4h-4M20 15v12"/><path d="M3 26h9M3 30h9M3 34h9M29 29h8v7h-8"/></svg>
    <div class="stat-num">$300M+</div><div class="stat-label">INVESTED</div><div class="stat-sub">In Property Renovations</div>
  </div>

  <h2 class="abs welcome-title">WELCOME TO VELMORA</h2>
  <p class="abs welcome-text">Velmora Partners Is A Vertically Integrated Real Estate Investment Firm With A Proven Four-Decade Track Record. We Acquire, Reposition, And Operate High-Performing Assets Across Multiple Sectors Always With A Focus On Exceptional, Risk-Adjusted Returns.</p>

  <section class="abs contact-panel">
    <h2 class="abs panel-title">GET IN TOUCH</h2>
    <div class="field" style="left:69px;top:81px;width:174px;height:31px"><svg viewBox="0 0 10 10" fill="none" stroke="#d71f27" stroke-width=".8"><circle cx="5" cy="3" r="2"/><path d="M1 9.5c0-3 8-3 8 0"/></svg>First Name</div>
    <div class="field" style="left:250px;top:81px;width:173px;height:31px"><svg viewBox="0 0 10 10" fill="none" stroke="#d71f27" stroke-width=".8"><circle cx="5" cy="3" r="2"/><path d="M1 9.5c0-3 8-3 8 0"/></svg>Last Name</div>
    <div class="field" style="left:69px;top:120px;width:174px;height:31px"><svg viewBox="0 0 10 10" fill="none" stroke="#d71f27" stroke-width=".8"><rect x="1" y="2.5" width="8" height="5.5"/><path d="M1 2.5l4 3 4-3"/></svg>Your Email</div>
    <div class="field" style="left:250px;top:120px;width:173px;height:31px"><svg viewBox="0 0 10 10" fill="none" stroke="#d71f27" stroke-width=".8"><path d="M2 1l2 2-1 1.5c1 1.5 2 2.5 3.5 3.5L8 6l2 2-1.5 1.5C5 9 1 5 .5 1.5z"/></svg>Phone</div>
    <div class="field" style="left:69px;top:159px;width:354px;height:63px"><svg viewBox="0 0 10 10" fill="none" stroke="#d71f27" stroke-width=".8"><path d="M5 1.5a4 3.3 0 11-2 6.2L1 8.8l.7-2A3.3 3.3 0 015 1.5z"/><path d="M3.3 4.5h3.4M3.3 6h2.4"/></svg>Your Message</div>
    <div class="abs btn submit">SUBMIT NOW</div>
  </section>

  <footer class="abs site-footer">
    <div class="abs brand">VELMORA</div>
    <nav class="abs footer-nav"><span>HOME</span><span>OUR STORY</span><span>INVESTMENT STRATEGY</span><span>WHAT SETS US APART</span><span>OUR PORTFOLIO</span><span>CONTACT US</span></nav>
    <div class="abs info" style="left:123px"><div class="info-icon"><svg viewBox="0 0 10 10" fill="#d71f27"><path d="M5 .5a3.3 3.3 0 00-3.3 3.3C1.7 6.3 5 9.5 5 9.5s3.3-3.2 3.3-5.7A3.3 3.3 0 005 .5zm0 4.5a1.2 1.2 0 110-2.4 1.2 1.2 0 010 2.4z"/></svg></div><div><b>ADDRESS</b><span>Cedar Point, NJ</span></div></div>
    <div class="abs info" style="left:233px"><div class="info-icon"><svg viewBox="0 0 10 10" fill="#d71f27"><path d="M2 .8l2 2-1 1.5c1 1.5 2 2.5 3.5 3.5L8 6.6l2 2-1.5 1.2C5 9.5.5 5 .2 1.5z"/></svg></div><div><b>PHONE</b><span>555 010 2468</span></div></div>
    <div class="abs info" style="left:351px"><div class="info-icon"><svg viewBox="0 0 10 10" fill="#d71f27"><rect x=".5" y="2" width="9" height="6.5" rx=".8"/><path d="M.8 2.5L5 5.5l4.2-3" stroke="#111" stroke-width=".7" fill="none"/></svg></div><div><b>EMAIL</b><span>info&#64;velmora&#46;com</span></div></div>
    <div class="abs btn career">CAREER INQUIRIES</div>
  </footer>
  <div class="abs divider"></div>
  <div class="abs copyright nowrap">© 2025 Velmora. All Rights Reserved.</div>
  <div class="abs social" style="left:535px" aria-label="Social profile 1"></div>
  <div class="abs social" style="left:555px" aria-label="Social profile 2"></div>
  <div class="abs social" style="left:575px" aria-label="Social profile 3"></div>
  <div class="abs social" style="left:595px" aria-label="Social profile 4"></div>
</div>
</body>
</html>
```